オリジナルデザインの暑中見舞いはがき
サイズ=120×235mm(一般的な洋長3封筒サイズ)
縦横どちらでも構いません。

★デザインリクエスト
①以下のサイト内の物件写真やロゴ等を自由に使用していただいて結構です。
・弊社の運営の賃貸募集サイト「MELU」https://melu-kashi.jp/
・弊社コーポレートサイト http://www.sorel-kt.co.jp/
②コピーの文面はおまかせします。社長の意向により何度か修正いただくかと思います。
③宛名面は、昨年のXmasカードと同様のデザインで内容の物件等だけ新しい情報に入れ替えしていただきます。
④夏らしさを感じるもの。
⑤2019年とわかること(2019年 盛夏など)を入れる
⑥8/11~8/15が夏季休業ということを入れる
⑦文字は明朝よりやわらかい印象のゴシック体、小さめにすっきりまとめて下さい。

メインの送付先は、建設会社、不動産関係、設計関係、不動産オーナーなどです。

参考として昨年の暑中見舞いとXmasカードを添付致します。

その他何かご不明な点がございましたら、お気軽にご質問下さい。
どうぞよろしくお願いいたします。
8月11日(日)より8月15日(木)まで夏季休業とさせていただきます。
2018Xmasカードの宛名面の画像を追加しました。
締めきり前日になりましたが、提案が1件もなく非常に焦っています。。
依頼内容や予算も今までとほぼ変わらないのですが、このようなことはなかったので、
もし作り手さん側から見てわからない点や要望等ありましたらご連絡いただければと思います。
よろしくお願いします。
素敵なデザインのご提案多数いただきありがとうございます。
いくつか検討させていただきましたが、もう少し別のデザインも見てみたいとのことで、
週明けまで締め切りを延長することにしました。
シンプルながら印象的なデザインがあればうれしいです。
参考として、以前使用したXmasカードも添付します。
引き続きよろしくお願いします。

ご提案ありがとうございました。
一見かわいらしいデザインですが、文字サイズや配置、色合いなど、全体的なバランスが丁寧で上品さがあり、選ばせていただきました。

締め切前日くらいまでご提案がなく、不安になってしまいましたが、
たくさん素敵なデザインをいただけてありがとうございました。
また、今年のXmasカード作成の際も利用させていただくので、
ご縁がありましたらぜひよろしくお願いいたします。

```html
<!DOCTYPE html>
<html lang="ja">
<head>
<meta charset="utf-8">
<title>暑中お見舞い 2019</title>
<link rel="stylesheet" href="https://fonts.googleapis.com/css2?family=Noto+Sans+JP:wght@500&family=Zen+Maru+Gothic:wght@500;700&display=swap">
<style>
  :root {
    --sky-deep: #1c6ccf;
    --sky-mid: #3c9fe6;
    --sky-light: #86d3f1;
    --dusk-lilac: #b9c3ee;
    --dusk-pink: #eaaad9;
    --city-top: #c2b4ea;
    --city-base: #8c80cc;
    --white: #ffffff;
    --greeting-yellow: #ffe600;
    --ink: #1d1d2b;
  }
  html, body {
    margin: 0;
    padding: 0;
    width: 1200px;
    height: 2344px;
    overflow: hidden;
  }
  .card {
    position: relative;
    width: 1200px;
    height: 2344px;
    overflow: hidden;
    font-family: "Zen Maru Gothic", "Noto Sans JP", sans-serif;
    background: linear-gradient(180deg,
      var(--sky-deep) 0%,
      var(--sky-mid) 30%,
      var(--sky-light) 55%,
      var(--dusk-lilac) 74%,
      var(--dusk-pink) 92%,
      #f3bfe0 100%);
  }
  .fireworks-sky {
    position: absolute;
    inset: 0;
  }
  .city-skyline {
    position: absolute;
    left: 0;
    right: 0;
    bottom: 0;
    height: 190px;
    background: linear-gradient(180deg, var(--city-top), var(--city-base));
    opacity: 0.85;
  }
  .season-kanji {
    position: absolute;
    left: 232px;
    top: 60px;
    margin: 0;
    font-family: "Noto Sans JP", sans-serif;
    font-weight: 500;
    font-size: 800px;
    line-height: 1;
    color: var(--white);
    transform-origin: top left;
    transform: scale(0.93, 1.95);
  }
  .greeting {
    position: absolute;
    left: 1018px;
    top: 110px;
    margin: 0;
    writing-mode: vertical-rl;
    font-size: 62px;
    font-weight: 700;
    letter-spacing: 12px;
    color: var(--greeting-yellow);
  }
  .holiday-notice {
    position: absolute;
    left: 134px;
    top: 236px;
    margin: 0;
    writing-mode: vertical-rl;
    font-size: 27px;
    font-weight: 500;
    letter-spacing: 3px;
    color: var(--white);
  }
  .message {
    position: absolute;
    left: 176px;
    top: 1848px;
    margin: 0;
    font-size: 24px;
    font-weight: 500;
    line-height: 46px;
    color: var(--ink);
  }
  .signature {
    position: absolute;
    right: 200px;
    top: 2002px;
    margin: 0;
    text-align: left;
    font-size: 21px;
    font-weight: 500;
    line-height: 40px;
    color: var(--ink);
  }
  .signature span { display: block; }
  .signature .date { padding-left: 98px; }
</style>
</head>
<body>
  <main class="card">
    <div class="fireworks-sky" role="img" aria-label="夜空に広がる花火のイラスト"></div>
    <div class="city-skyline" role="img" aria-label="タワーのある東京の街並みのシルエット"></div>

    <h1 class="season-kanji">夏</h1>

    <p class="greeting">暑中お見舞い申し上げます。</p>

    <p class="holiday-notice">八月十一日（土）より八月十九日（日）まで夏季休業とさせていただきます。</p>

    <p class="message">
      私たちは 2020 年の夏にむけ、東京をより魅力のある街へすべく<br>
      皆様とともに歩んでいく所存でございます。<br>
      酷暑の折、くれぐれもご健康とご自愛のほどお祈り申し上げます。
    </p>

    <p class="signature">
      <span class="date">令和元年 盛夏</span>
      <span class="name">代表取締役 CEO 森田浩一</span>
    </p>
  </main>
</body>
</html>
```